CREATE A KILLER WEBSITE DESIGN

We are a firearms training company that trains CIVILIANS (no police or military pictures - thank you!) to defend themselves and are looking for a killer design that's clean, easy to navigate and modern! We want the newest trends applied to this sight like a scrollable site so you can scroll down and see all the features. We are okay with tweaking the HTML but need the artistic design to look good. I'll provide a link to our current site along with a sight we really like so you can get an idea!

I'm supplying a PowerPoint Design we are going with from another designer so you can match the style to the new site.

PAGES: (Please use information from our current site. We like the information but just want a more polished look similar to the NWDLA site below but in our colors.)
Home - Long Form Scrolling Site. Top fold will be a video with a play button.
Falcon Institute - Seven Level Training Program Info Page That Will Contain A Video.
Contact Us - This will be a page that DOES NOT CONTAIN AN EMAIL ADDRESS. Just a contact us form
Meet The Trainer: Morgan Pellbrook

Our site:
https://www.brisklanewardens.biz

Sights We Like:
https://www.nwdefenseleague.example.com
https://quorvel.example.com
https://brantforgeworks.example.com
https://www.pelnrigear.example.com

Target Market(s)

Men and women ages 21 to 100 years old

Industry/Entity Type

Self Defense

Number of Pages Required

5+ page

Font styles to use
Sans Serif

Colors
f26267

Requirements
Must have
• Clean and engaging. Use of colors that match our logo.
Should not have
• Poor design quality

```html
<!DOCTYPE html>
<html lang="en">
<head>
<meta charset="UTF-8">
<title>Brisk Lane Wardens — Home</title>
<link href="https://fonts.googleapis.com/css2?family=Montserrat:wght@500;600;700;800&display=swap" rel="stylesheet">
<style>
  :root{
    --red:#e31414;
    --white:#ffffff;
    --teal-deep:#0c2f31;
    --teal:#1d4b4a;
    --teal-mid:#3c6560;
    --glow:#d8d6a6;
    --line:rgba(255,255,255,.55);
  }
  *{box-sizing:border-box;margin:0;padding:0}
  html,body{width:1200px;height:697px;overflow:hidden;background:var(--teal-deep)}
  body{font-family:'Montserrat',sans-serif;color:var(--white);position:relative}
  .hero-media{
    position:absolute;inset:0;
    background:
      radial-gradient(ellipse 260px 230px at 1010px 370px, rgba(232,230,190,.85), rgba(200,205,150,.35) 55%, transparent 80%),
      linear-gradient(100deg, var(--teal-deep) 0%, var(--teal) 45%, var(--teal-mid) 75%, #6f8a7a 100%);
  }
  .site-header{position:absolute;left:0;top:0;width:100%;height:100px}
  .brand{position:absolute;left:39px;top:48px;display:flex;align-items:center;gap:8px;
    font-weight:800;font-size:15px;letter-spacing:.5px;color:var(--white)}
  .brand-dot{width:22px;height:22px;border-radius:50%;background:var(--red)}
  .main-nav{position:absolute;top:55px;left:774px;display:flex;align-items:center;
    font-weight:600;font-size:11.5px;letter-spacing:1.8px}
  .main-nav a{color:var(--white);text-decoration:none}
  .nav-services{margin-right:30px}
  .nav-community{margin-right:30px}
  .nav-shop{margin-right:31px}
  .nav-cart{display:flex;align-items:center;gap:6px;margin-right:31px;margin-top:-4px}
  .section-nav{position:absolute;left:37px;top:288px;width:230px;height:334px}
  .section-nav .rail{position:absolute;left:11px;top:24px;width:1px;height:290px;background:var(--line)}
  .scroll-btn{position:absolute;left:0;width:23px;height:23px;border-radius:50%;background:var(--red);
    display:flex;align-items:center;justify-content:center}
  .scroll-up{top:0}
  .scroll-down{top:311px}
  .section-list{list-style:none;position:absolute;left:0;top:45px}
  .section-list li{display:flex;align-items:center;height:37.5px;font-size:12.5px;font-weight:500;letter-spacing:.2px}
  .section-list .marker{width:12px;height:12px;border-radius:50%;border:1.5px solid var(--white);
    background:var(--teal-deep);margin-left:5px;margin-right:14px;flex:none}
  .section-list li.active{font-weight:700;font-size:13.5px}
  .section-list li.active .marker{background:var(--white)}
  .hero-copy{position:absolute;left:397px;top:218px}
  .hero-title{font-weight:800;font-size:58px;line-height:57px;letter-spacing:.3px}
  .play{display:flex;align-items:center;gap:16px;margin-top:22px;font-weight:600;font-size:21px;letter-spacing:.3px}
  .play-btn{width:39px;height:39px;border-radius:50%;background:var(--red);display:flex;align-items:center;justify-content:center}
  .cta-row{display:flex;gap:32px;margin-top:22px}
  .btn{width:173px;height:37px;display:flex;align-items:center;justify-content:center;
    font-weight:600;font-size:11px;letter-spacing:.4px;color:var(--white);text-decoration:none}
  .btn-primary{background:var(--red)}
  .btn-outline{border:2px solid var(--red)}
  .chat-btn{position:absolute;left:1116px;top:606px;width:46px;height:46px;border-radius:50%;background:var(--red);
    display:flex;align-items:center;justify-content:center}
</style>
</head>
<body>
  <div class="hero-media" role="img" aria-label="Background video still: close-up of a cartridge leaving a muzzle with the company name printed on it and sparks around it"></div>

  <header class="site-header">
    <div class="brand"><span class="brand-dot"></span>BRISK LANE WARDENS</div>
    <nav class="main-nav">
      <a class="nav-services" href="#">SERVICES</a>
      <a class="nav-community" href="#">COMMUNITY</a>
      <a class="nav-shop" href="#">SHOP</a>
      <a class="nav-cart" href="#">
        <svg width="18" height="15" viewBox="0 0 18 15" fill="none" stroke="#fff" stroke-width="1.3"><path d="M1 1h3l2 9h9l2-6H5"/><circle cx="7" cy="13" r="1.2"/><circle cx="14" cy="13" r="1.2"/></svg>
        <span>0</span>
      </a>
      <a href="#">LOG IN</a>
    </nav>
  </header>

  <nav class="section-nav" aria-label="Page sections">
    <span class="rail"></span>
    <span class="scroll-btn scroll-up"><svg width="11" height="7" viewBox="0 0 11 7" fill="none" stroke="#fff" stroke-width="1.6"><path d="M1 6l4.5-4.5L10 6"/></svg></span>
    <ul class="section-list">
      <li class="active"><span class="marker"></span>Falcon Institute</li>
      <li><span class="marker"></span>About The Instructor</li>
      <li><span class="marker"></span>7 Levels Training</li>
      <li><span class="marker"></span>Upcoming Class</li>
      <li><span class="marker"></span>More On Video</li>
      <li><span class="marker"></span>Testimonial</li>
      <li><span class="marker"></span>Contact Us</li>
    </ul>
    <span class="scroll-btn scroll-down"><svg width="11" height="7" viewBox="0 0 11 7" fill="none" stroke="#fff" stroke-width="1.6"><path d="M1 1l4.5 4.5L10 1"/></svg></span>
  </nav>

  <main class="hero-copy">
    <h1 class="hero-title">Don't Settle<br>For A Gun<br>Shop Class!</h1>
    <div class="play">
      <span class="play-btn"><svg width="13" height="15" viewBox="0 0 13 15"><path d="M1 1l11 6.5L1 14z" fill="#fff"/></svg></span>
      <span>PLAY VIDEO</span>
    </div>
    <div class="cta-row">
      <a class="btn btn-primary" href="#">FALCON INSTITUTE</a>
      <a class="btn btn-outline" href="#">GET TICKETS NOW</a>
    </div>
  </main>

  <span class="chat-btn"><svg width="24" height="22" viewBox="0 0 24 22"><path d="M12 1C6 1 1.5 5 1.5 10s4.5 9 10.5 9c1.3 0 2.5-.2 3.6-.5L20 21l-.6-4.2C21.4 15 22.5 12.7 22.5 10 22.5 5 18 1 12 1z" fill="#fff"/><circle cx="8" cy="10" r="1.2" fill="#e31414"/><circle cx="12" cy="10" r="1.2" fill="#e31414"/><circle cx="16" cy="10" r="1.2" fill="#e31414"/></svg></span>
</body>
</html>
```